Business Card Design For A Renovation Contractor Company

We need a business card for a new company based in Singapore, our company name is "KT Planora". We are a renovation contractor that builds designs into reality. We build more of F&B restaurants, retail stores and commercial offices. We work very closely with designers. The final design should communicate to our client that we are a company that you can trust, that will plan and complete your project without giving you a headache. I like my client to remember my company as "KT". The beauty of SIMPLE is important.

Industry/Entity Type

Contractor

Requirements
Nice to have
• Black or Red base

```html
<!DOCTYPE html>
<html lang="en">
<head>
<meta charset="utf-8">
<title>KT Planora Business Card</title>
<link rel="stylesheet" href="https://fonts.googleapis.com/css2?family=Questrial&family=Open+Sans:wght@400;600&family=Libre+Baskerville:wght@700&display=swap">
<style>
  :root {
    --backdrop: #e7e4df;
    --card-dark: #262626;
    --card-light: #333333;
    --brand-red: #d0202e;
    --ink-white: #f4f4f4;
    --ink-grey: #b9b9b9;
    --rule-grey: #8a8a8a;
  }
  * { box-sizing: border-box; margin: 0; padding: 0; }
  html, body {
    width: 1200px;
    height: 723px;
    overflow: hidden;
    background: var(--backdrop);
  }
  .canvas {
    position: relative;
    width: 1200px;
    height: 723px;
    display: flex;
    justify-content: center;
    align-items: center;
    gap: 90px;
  }
  .card {
    position: relative;
    width: 330px;
    height: 566px;
    background: radial-gradient(circle at 40% 55%, var(--card-light), var(--card-dark) 75%);
    box-shadow: 0 10px 28px rgba(0,0,0,0.28);
  }

  /* Front */
  .card-front {
    display: flex;
    justify-content: center;
    align-items: center;
    gap: 14px;
  }
  .front-dot {
    width: 22px;
    height: 22px;
    border-radius: 50%;
    background: var(--brand-red);
  }
  .front-name {
    font-family: "Questrial", sans-serif;
    font-size: 42px;
    color: var(--ink-white);
    letter-spacing: 1px;
  }

  /* Back */
  .card-back { padding: 48px 30px 0 30px; }
  .brand-block {
    display: flex;
    flex-direction: column;
    align-items: flex-end;
  }
  .brand-row {
    display: flex;
    align-items: center;
    gap: 10px;
  }
  .brand-dot {
    width: 16px;
    height: 16px;
    border-radius: 50%;
    background: var(--brand-red);
  }
  .brand-name {
    font-family: "Questrial", sans-serif;
    font-size: 38px;
    color: var(--ink-white);
    line-height: 1;
  }
  .brand-rule {
    width: 250px;
    height: 1px;
    background: var(--rule-grey);
    margin: 8px 0 5px;
  }
  .brand-tagline {
    font-family: "Questrial", sans-serif;
    font-size: 16px;
    color: var(--ink-grey);
    letter-spacing: 0.5px;
  }
  .person {
    margin-top: 56px;
    text-align: right;
    padding-right: 40px;
  }
  .person-name {
    font-family: "Libre Baskerville", serif;
    font-size: 17px;
    color: var(--ink-white);
    letter-spacing: 0.5px;
  }
  .person-title {
    font-family: "Open Sans", sans-serif;
    font-weight: 600;
    font-size: 14px;
    color: var(--brand-red);
    margin-top: 3px;
  }
  .address {
    margin-top: 18px;
    text-align: right;
    padding-right: 40px;
    font-family: "Open Sans", sans-serif;
    font-size: 13.5px;
    line-height: 1.5;
    color: var(--ink-grey);
  }
  .contact-list {
    list-style: none;
    margin-top: 44px;
    padding-left: 30px;
    font-family: "Open Sans", sans-serif;
    font-size: 15px;
    line-height: 1.6;
    color: var(--ink-grey);
  }
  .contact-label {
    color: var(--brand-red);
    font-weight: 600;
    display: inline-block;
    width: 22px;
  }
</style>
</head>
<body>
  <main class="canvas">
    <section class="card card-front" aria-label="Card front">
      <span class="front-dot"></span>
      <span class="front-name">KT Planora</span>
    </section>

    <section class="card card-back" aria-label="Card back">
      <div class="brand-block">
        <div class="brand-row">
          <span class="brand-dot"></span>
          <span class="brand-name">KT Planora</span>
        </div>
        <div class="brand-rule"></div>
        <p class="brand-tagline">turning plans into spaces</p>
      </div>

      <div class="person">
        <p class="person-name">DANIEL TAN</p>
        <p class="person-title">President</p>
      </div>

      <p class="address">18 Kallang Bahru, #03-07<br>Singapore 339412</p>

      <ul class="contact-list">
        <li><span class="contact-label">T:</span> (65) 6123-4580</li>
        <li><span class="contact-label">F:</span> (65) 6123-4581</li>
        <li><span class="contact-label">E:</span> info@ktplanora.sg</li>
        <li><span class="contact-label">W:</span> www.ktplanora.sg</li>
      </ul>
    </section>
  </main>
</body>
</html>
```